Flyer Design For Quorra Tag Business

Our business needs a flyer design for a new company in Las Vegas, NV called "Quorra Tag Runners, LLC" Our mission and goal is to ensure that every customer that we serve is "Always First In Line". We want our customers to be able to spend their days at work or with family or doing other important duties instead of planning their day around the DMV or waiting at the DMV for 3-6 hours waiting to be served. Please refer to the attached business cards for ideas and the services that we provide to our customers. You may also email or comment on this project if you need more information and we will respond within 24 hours. In terms of the design, colors, layout, etc........ I say use your imagination. However, your design has to be eye-catching, unique, makes a statement, stands out, etc. We are very open to your ideas and we will provide feedback.

Thank you for your interest and time,

Quorra Tag Runners, LLC

Target Market(s)

The public

Industry/Entity Type

Business

Requirements
Must have
• It would be advisable to include cars, trucks, motorcycles, etc in your design. Otherwise, you may be asked to try again.

```html
<!DOCTYPE html>
<html lang="en">
<head>
<meta charset="utf-8">
<title>Quorra Tag Runners, LLC – Flyer</title>
<link href="https://fonts.googleapis.com/css2?family=Oswald:wght@500;600&family=Roboto:wght@400;500;700&family=Open+Sans:wght@600&display=swap" rel="stylesheet">
<style>
  :root{
    --teal:#13566e;
    --teal-deep:#0f4a60;
    --slate-dark:#23343d;
    --slate-light:#5a7683;
    --crimson:#e2104f;
    --crimson-dark:#b80c40;
    --white:#ffffff;
    --car-light:#ffc233;
    --car-dark:#d98a00;
  }
  *{margin:0;padding:0;box-sizing:border-box}
  html,body{width:928px;height:1200px;overflow:hidden;background:#ececec}
  .flyer{position:relative;width:928px;height:1200px;overflow:hidden;background:var(--white)}
  .flyer-shapes{position:absolute;inset:0}
  .car-visual{position:absolute;left:0;top:70px;width:590px;height:520px;
    border-radius:40% 45% 30% 25% / 30% 35% 45% 40%;
    background:radial-gradient(ellipse at 45% 60%,var(--car-light) 0%,#f5a800 45%,var(--car-dark) 75%,rgba(217,138,0,0) 100%)}
  .brand{position:absolute;left:504px;width:400px;top:92px;text-align:center;color:var(--white);font-family:"Roboto",sans-serif}
  .brand-name{font-size:52px;font-weight:700;line-height:1}
  .brand-sub{font-size:34px;font-weight:500;line-height:1.3}
  .brand-sub span{font-weight:400}
  .tagline{position:absolute;left:560px;top:296px;width:326px;text-align:center;color:var(--white);font-family:"Oswald",sans-serif;line-height:1.15}
  .tagline-strong{font-size:42px;font-weight:600;display:block}
  .tagline-light{font-family:"Roboto",sans-serif;font-size:38px;font-weight:400;display:block}
  .services-title{position:absolute;left:311px;top:626px;width:300px;text-align:center;font-family:"Oswald",sans-serif;font-weight:600;font-size:50px;color:var(--teal);line-height:1.2}
  .service-list{position:absolute;list-style:none;font-family:"Open Sans",sans-serif;font-weight:600;font-size:24px;color:var(--white)}
  .service-list li{height:35px;line-height:35px;display:flex;align-items:center}
  .service-list svg{width:22px;height:16px;margin-right:14px;flex:none}
  .service-list--left{left:104px;top:690px}
  .service-list--right{left:492px;top:690px}
  .service-list--right svg{margin-right:10px}
  .owner{position:absolute;left:0;width:928px;top:910px;text-align:center;font-family:"Oswald",sans-serif;font-weight:600;font-size:66px;line-height:1.2;color:var(--teal);letter-spacing:0.5px}
  .owner-role{color:var(--crimson)}
  .phone{position:absolute;left:0;width:928px;top:988px;display:flex;justify-content:center;align-items:center;gap:8px;font-family:"Roboto",sans-serif;font-weight:500;font-size:42px;color:var(--teal);letter-spacing:1px}
  .phone svg{width:32px;height:32px}
  .contact{position:absolute;left:498px;top:1100px;font-family:"Roboto",sans-serif;font-size:22px;color:var(--white);line-height:30px;list-style:none}
  .contact li{display:flex;align-items:center;gap:10px}
  .contact svg{width:24px;height:18px}
</style>
</head>
<body>
<main class="flyer">
  <svg class="flyer-shapes" width="928" height="1200" viewBox="0 0 928 1200" aria-hidden="true">
    <defs>
      <radialGradient id="hero-glow" cx="620" cy="190" r="620" gradientUnits="userSpaceOnUse">
        <stop offset="0" stop-color="var(--slate-light)"/>
        <stop offset="1" stop-color="var(--slate-dark)"/>
      </radialGradient>
    </defs>
    <rect class="hero-backdrop" x="0" y="0" width="928" height="680" fill="url(#hero-glow)"/>
    <path class="hero-band-teal" d="M0 600 C260 620 520 500 928 470 L928 560 C560 560 300 690 0 700 Z" fill="var(--teal)"/>
    <path class="hero-band-red" d="M600 515 C720 470 830 470 928 490 L928 520 C820 505 720 510 600 515 Z" fill="var(--crimson)"/>
    <path class="hero-white" d="M0 690 C300 680 560 560 928 550 L928 1200 L0 1200 Z" fill="var(--white)"/>
    <path class="tag-tail" d="M800 450 L902 450 L902 500 L860 600 L852 470 Z" fill="var(--crimson-dark)"/>
    <rect class="tag-box" x="544" y="262" width="358" height="200" rx="26" fill="var(--crimson)"/>
    <rect class="tag-stitch" x="556" y="274" width="334" height="176" rx="18" fill="none" stroke="var(--white)" stroke-width="2" stroke-dasharray="7 6"/>
    <rect class="services-panel" x="26" y="664" width="422" height="226" rx="30" fill="var(--crimson)"/>
    <rect class="services-panel" x="462" y="664" width="440" height="226" rx="30" fill="var(--crimson)"/>
    <rect class="services-tab" x="311" y="624" width="300" height="66" rx="28" fill="var(--white)"/>
    <path class="footer-band-teal" d="M0 1100 C300 1120 620 1050 928 980 L928 1200 L0 1200 Z" fill="var(--teal)"/>
    <path class="footer-line" d="M40 1110 C260 1150 600 1090 928 1010" fill="none" stroke="var(--white)" stroke-width="3" opacity="0.7"/>
    <path class="footer-swoosh-red" d="M44 1020 C50 1090 180 1130 560 1080 C300 1105 110 1100 44 1020 Z" fill="var(--crimson)"/>
  </svg>

  <div class="car-visual" role="img" aria-label="Photo of a yellow sports car with its scissor doors raised"></div>

  <header class="brand">
    <div class="brand-name">Quorra Tag</div>
    <div class="brand-sub">Runners <span>LLC</span></div>
  </header>

  <p class="tagline">
    <span class="tagline-strong">YOU’RE ALWAYS</span>
    <span class="tagline-light">FIRST IN LINE</span>
  </p>

  <h2 class="services-title">SERVICES</h2>

  <ul class="service-list service-list--left">
    <li><svg viewBox="0 0 22 16"><path d="M0 5h12V0l10 8-10 8v-5H0z" fill="#fff"/></svg>Titles</li>
    <li><svg viewBox="0 0 22 16"><path d="M0 5h12V0l10 8-10 8v-5H0z" fill="#fff"/></svg>Plates</li>
    <li><svg viewBox="0 0 22 16"><path d="M0 5h12V0l10 8-10 8v-5H0z" fill="#fff"/></svg>Registrations</li>
    <li><svg viewBox="0 0 22 16"><path d="M0 5h12V0l10 8-10 8v-5H0z" fill="#fff"/></svg>Moving Permits</li>
    <li><svg viewBox="0 0 22 16"><path d="M0 5h12V0l10 8-10 8v-5H0z" fill="#fff"/></svg>Disabled Placar</li>
  </ul>

  <ul class="service-list service-list--right">
    <li><svg viewBox="0 0 22 16"><path d="M0 5h12V0l10 8-10 8v-5H0z" fill="#fff"/></svg>Vehicle Purchases</li>
    <li><svg viewBox="0 0 22 16"><path d="M0 5h12V0l10 8-10 8v-5H0z" fill="#fff"/></svg>Insurance Lapses &amp; SR-22</li>
    <li><svg viewBox="0 0 22 16"><path d="M0 5h12V0l10 8-10 8v-5H0z" fill="#fff"/></svg>ID's and Driver's License</li>
    <li><svg viewBox="0 0 22 16"><path d="M0 5h12V0l10 8-10 8v-5H0z" fill="#fff"/></svg>Dash Pass</li>
    <li><svg viewBox="0 0 22 16"><path d="M0 5h12V0l10 8-10 8v-5H0z" fill="#fff"/></svg>Pickup &amp; Delivery Available</li>
  </ul>

  <p class="owner">DALEN MARSH <span class="owner-role">OWNER</span></p>

  <p class="phone">
    <svg viewBox="0 0 32 32" aria-hidden="true"><rect width="32" height="32" rx="6" fill="var(--teal)"/><path d="M11 7c1 0 2 3 2.5 4.5.3 1-1.5 2-1.3 2.8.6 2 2.5 4 4.5 4.6.8.2 1.8-1.6 2.8-1.3C21 18 25 19 25 20c0 2-2 4.5-4 4.5C13.5 24.5 7.5 18.5 7.5 11 7.5 9 9.5 7 11 7z" fill="#fff"/></svg>
    702-555-0147
  </p>

  <ul class="contact">
    <li><svg viewBox="0 0 24 18" aria-hidden="true"><rect x="1" y="1" width="22" height="16" fill="none" stroke="#fff" stroke-width="2"/><path d="M1 1l11 9 11-9" fill="none" stroke="#fff" stroke-width="2"/></svg>Info@QuorraTagRunners.com</li>
    <li><svg viewBox="0 0 24 18" aria-hidden="true"><circle cx="12" cy="9" r="8" fill="none" stroke="#fff" stroke-width="1.6"/><ellipse cx="12" cy="9" rx="3.5" ry="8" fill="none" stroke="#fff" stroke-width="1.4"/><path d="M4 9h16M5.5 5h13M5.5 13h13" stroke="#fff" stroke-width="1.2"/></svg>www.QuorraTagRunners.com</li>
  </ul>
</main>
</body>
</html>
```